Comic, writer, and entrepreneur based in Los Angeles, CA

UPDATED BRIEF:

Need a PROFESSIONAL yet simultaneously sexy business card that will inspire those to go to my social media accounts and follow me.

Need all of my social media (logos on card, please) As well as my picture, which I will provide.

If there is a way where you could scan the business card from your phone and it would take you to the social media accounts that would be great too!

My goal is to get a comedy writing job at the Nightly Desk or WLR and also go on Pelican Pond once my app is fully functional and created.

But the business card is just something to give people when I am making connections in both the entrepreneurial world as well as the comedy world so it has to help me stand out in that way :).

#: 417-552-8904
Email: kbellin@mx.ovrk.edu
Pictogram: Rosalind_Q.K
Chirpr: @ThePalermoNotes
Craftlo: Rosa’s Clever Tops (website: https://www.craftlo-example.com/shop/RosasTp?ref=pr_shop_more)
VidStream: The Gagmistress (website: https://www.vidstream-example.com/channel/QRpLwVn4kZ-mTHbyqo8erxt7B )
Friendlink: /rosalind.bellin.71924
Website App: WarmFixerFolk.example (app in progress. Need emails to make a prototype.)

Target Market(s)

Talent agents needing TV writers and TV comedy personalities. Investors for my app.

Industry/Entity Type

Tv

Contact Information for Business Card

Can be double or single sided, whichever looks best. Green is my favorite color but I am open to anything. Maybe silver and green?! Just make it classy and sexy.

Colors

Designer to choose colors to be used in the design.

Requirements
Must have
• Chirpr: ThePalermoNotes
• Pictogram: Rosalind_q.k
• Vidstream: The Gagmistress
• Email: kbellin@mx.ovrk.edu
• Phone: 417-552-8904
• writer, comic, entrepreneur--or--comedy writer and entrepeneur
Nice to have
• Make me standout. I'm a star ;-). Please check out my social media for files or ideas. Thanks.

```html
<!DOCTYPE html>
<html lang="en">
<head>
<meta charset="utf-8">
<title>Rosalind — Business Card</title>
<link rel="stylesheet" href="https://fonts.googleapis.com/css2?family=Roboto:wght@400;500;700&display=swap">
<style>
  :root {
    --backdrop: #d9dadb;
    --card-pink: #d8348f;
    --card-pink-light: #e75aa8;
    --photo-tone: #f2a9cf;
    --photo-tone-deep: #c92f82;
    --ink: #ffffff;
  }
  * { margin: 0; padding: 0; box-sizing: border-box; }
  html, body {
    width: 1200px; height: 900px; overflow: hidden;
    background: var(--backdrop);
    font-family: "Roboto", Arial, sans-serif;
    color: var(--ink);
  }
  .canvas { position: relative; width: 1200px; height: 900px; }
  .card {
    position: absolute; left: 340px; width: 518px; height: 297px;
    background: radial-gradient(ellipse at 50% 50%, var(--card-pink-light) 0%, var(--card-pink) 70%);
    box-shadow: 6px 8px 14px rgba(0,0,0,0.28);
  }
  .card--front { top: 128px; }
  .card--back { top: 485px; }

  /* Front */
  .portrait {
    position: absolute; left: 50%; top: 28px; transform: translateX(-50%);
    width: 116px; height: 116px; border-radius: 50%;
    border: 4px solid var(--ink);
    background: radial-gradient(circle at 50% 40%, var(--photo-tone) 0%, var(--photo-tone-deep) 100%);
  }
  .identity {
    position: absolute; left: 0; right: 0; top: 160px;
    text-align: center;
  }
  .identity__name { font-size: 34px; font-weight: 700; letter-spacing: 3px; line-height: 40px; }
  .identity__title {
    margin-top: 8px; font-size: 13px; font-weight: 500;
    letter-spacing: 2px; text-transform: uppercase;
  }

  .web-rule {
    position: absolute; left: 0; right: 0; top: 274px;
    display: flex; align-items: center; gap: 10px;
  }
  .web-rule__line { flex: 1; height: 3px; background: var(--ink); }
  .web-rule__line--left { flex: 0 0 185px; }
  .web-rule__text { font-size: 15px; font-weight: 500; letter-spacing: 0.5px; }

  /* Back */
  .brand {
    position: absolute; left: 0; width: 241px; top: 118px;
    display: flex; flex-direction: column; align-items: center;
  }
  .brand__row { display: flex; align-items: center; gap: 8px; }
  .brand__mark { width: 22px; height: 22px; border-radius: 50%; border: 3px solid var(--ink); }
  .brand__name { font-size: 22px; font-weight: 700; letter-spacing: 2px; line-height: 26px; }
  .brand__title {
    margin-top: 10px; font-size: 10px; font-weight: 500;
    letter-spacing: 1px; text-transform: uppercase;
  }

  .divider {
    position: absolute; left: 241px; top: 40px;
    width: 3px; height: 217px; background: var(--ink);
  }
  .contact-list { list-style: none; position: absolute; left: 266px; top: 40px; }
  .contact-list__item {
    display: flex; align-items: center; gap: 10px;
    height: 26px; margin-bottom: 12px;
    font-size: 12px; font-weight: 500; text-transform: uppercase; letter-spacing: 0.3px;
    white-space: nowrap;
  }
  .contact-list__icon { width: 24px; height: 24px; flex: none; }
  .contact-list__dot {
    width: 14px; height: 14px; margin: 0 5px; flex: none;
    border-radius: 50%; border: 2px solid var(--ink);
  }
</style>
</head>
<body>
<main class="canvas">
  <section class="card card--front" aria-label="Business card front">
    <div class="portrait" role="img" aria-label="Portrait photo of Rosalind"></div>
    <div class="identity">
      <p class="identity__name">ROSALIND</p>
      <p class="identity__title">Comedy Writer &amp; Entrepreneur</p>
    </div>
    <div class="web-rule">
      <span class="web-rule__line web-rule__line--left"></span>
      <span class="web-rule__text">web. mx.ovrk.edu</span>
      <span class="web-rule__line"></span>
    </div>
  </section>

  <section class="card card--back" aria-label="Business card back">
    <div class="brand">
      <div class="brand__row">
        <span class="brand__mark"></span>
        <span class="brand__name">ROSALIND</span>
      </div>
      <p class="brand__title">Writer · Comic · Entrepreneur</p>
    </div>
    <span class="divider"></span>
    <ul class="contact-list">
      <li class="contact-list__item">
        <svg class="contact-list__icon" viewBox="0 0 24 24" fill="none" stroke="#fff" stroke-width="1.6">
          <rect x="2" y="5" width="20" height="14"/>
          <path d="M2 5 L12 13 L22 5"/>
        </svg>
        kbellin@mx.ovrk.edu
      </li>
      <li class="contact-list__item">
        <svg class="contact-list__icon" viewBox="0 0 24 24" fill="none" stroke="#fff" stroke-width="1.6">
          <rect x="7" y="2" width="10" height="20" rx="2"/>
          <rect x="9" y="5" width="6" height="11" fill="#fff" stroke="none"/>
          <circle cx="12" cy="19" r="0.9" fill="#fff"/>
        </svg>
        417-552-8904
      </li>
      <li class="contact-list__item">
        <svg class="contact-list__icon" viewBox="0 0 24 24" fill="none" stroke="#fff" stroke-width="1.5">
          <circle cx="12" cy="12" r="9.5"/>
          <ellipse cx="12" cy="12" rx="4.2" ry="9.5"/>
          <path d="M2.5 12 H21.5 M4 7 H20 M4 17 H20"/>
        </svg>
        mx.ovrk.edu
      </li>
      <li class="contact-list__item">
        <span class="contact-list__dot"></span>
        Chirpr @ThePalermoNotes
      </li>
      <li class="contact-list__item">
        <span class="contact-list__dot"></span>
        Pictogram Rosalind_q.k
      </li>
      <li class="contact-list__item">
        <span class="contact-list__dot"></span>
        Vidstream The Gagmistress
      </li>
    </ul>
  </section>
</main>
</body>
</html>
```